A NEW UPDATED VERSION OF A 4"X9" RACK CARD

A NEW UPDATED VERSION OF A RACK CARD, THIS CARD IS 5 YEARS OLD AND WE WANT SOMETHING NEW AND FRESH AND MORE UPDATED TO TODAY. MARKET TO A YOUNGER CROWD. USE THE ATTACHED RACK CARD FOR THE INFO AND VERBAGE AND LOGO TO BE USED. DO NOT USE THE PICTURE OF THE BUILDIING, don't use the picture of the 2 guys. USED THE ATTACHED POST CARDS AS COLORS AND REFERENCE.

Target Market(s)

25-45

Industry/Entity Type

HOME INSPECTIONS

```html
<!DOCTYPE html>
<html lang="en">
<head>
<meta charset="utf-8">
<title>Keystone Home Inspections – 11-Month Reminder Rack Card</title>
<link rel="stylesheet" href="https://fonts.googleapis.com/css2?family=Poppins:ital,wght@0,400;0,500;0,600;0,700;0,800;1,400;1,700;1,800&display=swap">
<style>
  :root {
    --bg: #ececec;
    --navy: #1b3766;
    --red: #b01e2e;
    --red-deep: #8c1622;
    --red-bright: #d7303f;
    --blue: #1f63c0;
    --blue-deep: #123f86;
    --sky: #dfe9f3;
    --pink: #f6dfe2;
    --white: #ffffff;
  }
  * { box-sizing: border-box; margin: 0; padding: 0; }
  html, body { width: 1200px; height: 800px; overflow: hidden; }
  body {
    background: var(--bg);
    font-family: "Poppins", sans-serif;
    display: flex; align-items: center; justify-content: center;
  }
  .rack-card {
    position: relative;
    width: 340px; height: 765px;
    overflow: hidden;
    background: linear-gradient(160deg, var(--pink) 0%, var(--white) 45%, var(--sky) 100%);
    box-shadow: 0 10px 30px rgba(0,0,0,.12);
  }
  .top-flap { position: absolute; left: 0; top: 0; width: 340px; height: 110px; }
  .brand {
    position: absolute; top: 62px; left: 0; right: 0;
    display: flex; align-items: center; justify-content: center; gap: 6px;
    font-weight: 700; font-size: 13px; color: var(--navy);
  }
  .brand-dot { width: 10px; height: 10px; border-radius: 50%; background: var(--red); }
  .eyebrow {
    position: absolute; top: 116px; left: 0; right: 0; text-align: center;
    color: var(--red-bright); font-weight: 700; font-size: 11px; letter-spacing: 3px;
  }
  .headline {
    position: absolute; top: 132px; left: 0; right: 0; text-align: center;
    color: var(--navy); font-weight: 800; font-size: 29px; line-height: 1.15;
  }
  .tagline {
    position: absolute; top: 218px; left: 0; right: 0; text-align: center;
    color: var(--navy); font-style: italic; font-size: 14px;
  }
  .body-panel {
    position: absolute; left: 0; top: 296px; width: 340px; height: 469px;
    background: linear-gradient(180deg, var(--red) 0%, var(--red-deep) 55%, var(--red) 100%);
  }
  .house-photo {
    position: absolute; inset: 0;
    background: radial-gradient(ellipse at 50% 40%, rgba(255,255,255,.10), rgba(0,0,0,0) 70%);
  }
  .frame-line { position: absolute; top: 0; width: 1px; height: 420px; background: rgba(255,255,255,.55); }
  .frame-line.left { left: 50px; }
  .frame-line.right { left: 290px; }
  .reminder { position: absolute; left: 0; top: 258px; width: 340px; height: 64px; }
  .reminder-text {
    position: absolute; left: 26px; top: 271px; color: var(--white);
  }
  .reminder-text .months { font-weight: 800; font-size: 22px; line-height: 1.05; }
  .reminder-text .label { font-weight: 700; font-size: 12px; line-height: 1.3; }
  .ribbon {
    position: absolute; left: 0; width: 340px; background: var(--white);
    color: var(--navy); font-weight: 800; font-style: italic; text-align: center;
  }
  .ribbon.warranty { top: 329px; height: 24px; line-height: 24px; font-size: 11px; }
  .ribbon.schedule { top: 568px; height: 40px; font-size: 13px; line-height: 1.2; padding-top: 3px; color: var(--blue-deep); }
  .congrats {
    position: absolute; top: 362px; left: 0; right: 0; text-align: center;
    color: var(--white); font-weight: 800; font-style: italic; font-size: 15px; line-height: 1.2;
  }
  .intro {
    position: absolute; top: 406px; left: 58px; width: 224px;
    color: var(--white); font-size: 7.6px; font-weight: 500; line-height: 1.38;
    text-align: justify; text-indent: 28px;
  }
  .benefits { position: absolute; top: 620px; left: 20px; width: 300px; list-style: none; }
  .benefits li {
    display: flex; align-items: flex-start; gap: 10px;
    color: var(--white); font-size: 10.5px; font-weight: 500; line-height: 1.15; margin-bottom: 4px;
  }
  .benefits svg { flex: 0 0 14px; margin-top: 0; }
  .contact-bar {
    position: absolute; left: 30px; top: 728px; width: 280px; height: 37px;
    background: linear-gradient(180deg, var(--blue) 0%, var(--blue-deep) 100%);
    border-radius: 10px 10px 0 0;
    display: flex; align-items: center; justify-content: space-around;
    color: var(--white); font-size: 9.5px; font-weight: 500;
  }
  .contact-item { display: flex; align-items: center; gap: 5px; }
</style>
</head>
<body>
  <article class="rack-card">
    <svg class="top-flap" viewBox="0 0 340 110" aria-hidden="true">
      <path d="M0 0 H340 V40 Q170 110 0 40 Z" fill="#dbe6f1"/>
      <path d="M0 40 Q170 110 340 40" fill="none" stroke="#c9d6e4" stroke-width="1.5"/>
    </svg>
    <div class="brand"><span class="brand-dot"></span>Keystone Home Inspections</div>
    <p class="eyebrow">YOUR TRUSTED</p>
    <h1 class="headline">HOME INSPECTION<br>EXPERTS</h1>
    <p class="tagline">“Protect Your Investment!”</p>

    <section class="body-panel">
      <div class="house-photo" role="img" aria-label="Faint photo of a new home behind red overlay"></div>
      <span class="frame-line left"></span>
      <span class="frame-line right"></span>
    </section>

    <svg class="reminder" viewBox="0 0 340 64" aria-hidden="true">
      <defs>
        <linearGradient id="bandRed" x1="0" x2="1">
          <stop offset="0" stop-color="#b01e2e"/><stop offset="1" stop-color="#d7303f"/>
        </linearGradient>
      </defs>
      <path d="M286 2 H318 L336 26 L318 50 H286 Z" fill="#1f63c0"/>
      <path d="M0 8 H296 L314 32 L296 58 H0 Z" fill="url(#bandRed)"/>
    </svg>
    <div class="reminder-text">
      <div class="months">11-Months</div>
      <div class="label">Home Inspection Reminder</div>
    </div>

    <div class="ribbon warranty">Don’t Let Your Builder’s Warranty Expire!</div>
    <h2 class="congrats">Congratulations on<br>Your New Home!</h2>
    <p class="intro">Lorem ipsum dolor sit amet, consectetuer adipiscing elit, sed diam nonummy nibh euismod tincidunt ut laoreet dolore magna aliquam erat volutpat. Ut wisi enim ad minim veniam, quis nostrud exerci tation ullamcorper suscipit lobortis nisl ut aliquip ex ea commodo consequat. Duis autem vel eum iriure dolor in hendrerit in vulputate velit esse molestie consequat, vel illum dolore eu feugiat nulla facilisis at vero eros et accumsan et iusto odio dignissim qui blandit praesent luptatum zzril delenit augue duis dolore te feugait nulla facilisi. Lorem ipsum dolor sit amet, cons ectetuer adipiscing elit, sed diam nonummy nibh euismod tincidunt ut laoreet dolore magna aliquam erat</p>
    <div class="ribbon schedule">Schedule your 11-Months<br>Inspections Today!</div>

    <ul class="benefits">
      <li><svg width="14" height="14" viewBox="0 0 14 14"><circle cx="7" cy="7" r="7" fill="#fff"/><path d="M7 3l1.1 2.5 2.6.2-2 1.7.6 2.6L7 8.6 4.7 10l.6-2.6-2-1.7 2.6-.2z" fill="#1b3766"/></svg>Early detection of hidden defects</li>
      <li><svg width="14" height="14" viewBox="0 0 14 14"><circle cx="7" cy="7" r="7" fill="#fff"/><path d="M7 3l1.1 2.5 2.6.2-2 1.7.6 2.6L7 8.6 4.7 10l.6-2.6-2-1.7 2.6-.2z" fill="#1b3766"/></svg>Maximize your builder’s warranty coverage</li>
      <li><svg width="14" height="14" viewBox="0 0 14 14"><circle cx="7" cy="7" r="7" fill="#fff"/><path d="M7 3l1.1 2.5 2.6.2-2 1.7.6 2.6L7 8.6 4.7 10l.6-2.6-2-1.7 2.6-.2z" fill="#1b3766"/></svg>Protect your investment</li>
      <li><svg width="14" height="14" viewBox="0 0 14 14"><circle cx="7" cy="7" r="7" fill="#fff"/><path d="M7 3l1.1 2.5 2.6.2-2 1.7.6 2.6L7 8.6 4.7 10l.6-2.6-2-1.7 2.6-.2z" fill="#1b3766"/></svg>Ensure a safe and comfortable living environment</li>
      <li><svg width="14" height="14" viewBox="0 0 14 14"><circle cx="7" cy="7" r="7" fill="#fff"/><path d="M7 3l1.1 2.5 2.6.2-2 1.7.6 2.6L7 8.6 4.7 10l.6-2.6-2-1.7 2.6-.2z" fill="#1b3766"/></svg>Expert advice and recommendations</li>
    </ul>

    <footer class="contact-bar">
      <span class="contact-item">
        <svg width="11" height="11" viewBox="0 0 12 12" aria-hidden="true"><circle cx="6" cy="6" r="5.2" fill="none" stroke="#fff" stroke-width="1.1"/><ellipse cx="6" cy="6" rx="2.3" ry="5.2" fill="none" stroke="#fff" stroke-width="1"/><path d="M1 6h10" stroke="#fff" stroke-width="1"/></svg>
        KeystoneHomeInspect.com
      </span>
      <span class="contact-item">
        <svg width="11" height="11" viewBox="0 0 12 12" aria-hidden="true"><path d="M2.5 1h2l1 2.6-1.3 1a6.5 6.5 0 0 0 3.2 3.2l1-1.3 2.6 1v2A1.5 1.5 0 0 1 9.5 11 8.5 8.5 0 0 1 1 2.5 1.5 1.5 0 0 1 2.5 1z" fill="#fff"/></svg>
        555-010-4821
      </span>
    </footer>
  </article>
</body>
</html>
```